Cleaning Company needs a new business card design

Hi, We are looking for new business card designs to update with our latest logo and company information.
We would like to see designs using the colours:
Royal Blue #4169E1 - this is our company colour so this has to be in there. Please feel free to experiment with other colours.
Must include:
Front of business card:
Logo
Back of the business card:
0800 529 6081
07438 915 702
Email: info@pkrtidyhomes.co.uk
Web: www.pkrtidyhomes.co.uk
Services:
End of Tenancy
Carpet & Upholstery
Regular & One Off
all work fully insured.
The front of the business card with the logo can be made to look raised print. The blue man to be a shiny finish.
The business card needs to be presented in a matt finish
The business must be in the following styles:
Standard Square with rounded corners.
Thank you to all that take part in this.
Target Market(s)
Men and Women of different ages in the UK.
Industry/Entity Type
House Cleaning
Contact Information for Business Card
Front of business card:
Logo
0800 529 6081
07438 915 702
Email: pkrtidy@mailbox-demo.co.uk
Services:
End of Tenancy
Carpet & Upholstery
Regular & One Off
all work fully insured.

```html
<!DOCTYPE html>
<html lang="en">
<head>
<meta charset="utf-8">
<title>PKR Tidy Homes – Business Card</title>
<link rel="stylesheet" href="https://fonts.googleapis.com/css2?family=Open+Sans:wght@400;600;700;800&display=swap">
<style>
  :root {
    --page: #3a3a3c;
    --card: #000000;
    --royal: #3a4fb8;
    --sky: #29a9e1;
    --white: #ffffff;
  }
  * { margin: 0; padding: 0; box-sizing: border-box; }
  html, body { width: 1200px; height: 900px; overflow: hidden; }
  body {
    background: var(--page);
    font-family: "Open Sans", Arial, sans-serif;
    display: flex;
    align-items: center;
    justify-content: center;
    gap: 60px;
  }
  .card {
    width: 480px;
    height: 480px;
    background: var(--card);
    border-radius: 30px;
    position: relative;
    color: var(--white);
    box-shadow: 0 10px 30px rgba(0,0,0,.45);
  }
  /* Front */
  .card-front .brand {
    position: absolute;
    left: 60px;
    top: 110px;
    display: flex;
    align-items: center;
    gap: 16px;
  }
  .brand-dot {
    width: 46px; height: 46px;
    border-radius: 50%;
    background: var(--royal);
    flex: none;
  }
  .brand-name {
    color: var(--royal);
    font-weight: 700;
    font-size: 40px;
    line-height: 1.05;
  }
  .services {
    position: absolute;
    left: 0; right: 0;
    top: 290px;
    text-align: center;
    font-weight: 600;
    font-size: 19px;
    line-height: 1.4;
    letter-spacing: .5px;
  }
  /* Back */
  .mark-circle {
    position: absolute;
    right: 110px;
    top: 50px;
    width: 120px; height: 120px;
    border-radius: 50%;
    background: var(--sky);
  }
  .contact-block {
    position: absolute;
    left: 40px;
    bottom: 40px;
  }
  .person-name {
    font-weight: 800;
    font-size: 30px;
    letter-spacing: 1px;
    line-height: 1.1;
  }
  .person-role {
    color: var(--sky);
    font-weight: 700;
    font-size: 20px;
    margin-bottom: 10px;
  }
  .contact-list { list-style: none; }
  .contact-list li {
    display: flex;
    align-items: center;
    gap: 12px;
    font-weight: 600;
    font-size: 19px;
    line-height: 1.35;
  }
  .contact-list svg { width: 16px; height: 16px; flex: none; }
</style>
</head>
<body>

  <section class="card card-front">
    <div class="brand">
      <span class="brand-dot"></span>
      <span class="brand-name">PKR Tidy Homes<br>Limited</span>
    </div>
    <p class="services">
      Services:<br>
      End of Tenancy<br>
      Carpet &amp; Upholstery<br>
      Regular &amp; One Off
    </p>
  </section>

  <section class="card card-back">
    <span class="mark-circle"></span>
    <div class="contact-block">
      <p class="person-name">HELEN MARSH</p>
      <p class="person-role">Director</p>
      <ul class="contact-list">
        <li>
          <svg viewBox="0 0 16 16"><path d="M3 1.5l3 .5 1 3-1.8 1.3a9 9 0 0 0 4.5 4.5L11 9l3 1 .5 3-1.5 1.5C7 14.5 1.5 9 1.5 3z" fill="none" stroke="var(--sky)" stroke-width="1.6"/></svg>
          0800 529 6081
        </li>
        <li>
          <svg viewBox="0 0 16 16"><rect x="4" y="1" width="8" height="14" rx="1.5" fill="none" stroke="var(--sky)" stroke-width="1.6"/><circle cx="8" cy="12.3" r="1" fill="var(--sky)"/></svg>
          07438 915 702
        </li>
        <li>
          <svg viewBox="0 0 16 16"><rect x="1" y="3" width="14" height="10" rx="1" fill="none" stroke="var(--sky)" stroke-width="1.6"/><path d="M1.5 3.5L8 9l6.5-5.5" fill="none" stroke="var(--sky)" stroke-width="1.6"/></svg>
          pkrtidy@mailbox-demo.co.uk
        </li>
        <li>
          <svg viewBox="0 0 16 16"><circle cx="8" cy="8" r="6.5" fill="none" stroke="var(--sky)" stroke-width="1.5"/><ellipse cx="8" cy="8" rx="2.8" ry="6.5" fill="none" stroke="var(--sky)" stroke-width="1.3"/><path d="M1.5 8h13" stroke="var(--sky)" stroke-width="1.3"/></svg>
          www.pkrtidyhomes.co.uk
        </li>
      </ul>
    </div>
  </section>

</body>
</html>
```